Business Consulting Business Card

professional business card with basic information (1) First and Last name (2) email address, (3) phone number, (4) website.

```html
<!DOCTYPE html>
<html lang="en">
<head>
<meta charset="utf-8">
<title>Business Card – Tidal Crest</title>
<link href="https://fonts.googleapis.com/css2?family=Lato:wght@400;700&display=swap" rel="stylesheet">
<style>
  :root{
    --page-bg:#e6e2dc;
    --card-bg:#eceae6;
    --panel-dark:#17303d;
    --panel-mid:#234556;
    --accent-teal:#2f9a8f;
    --text-muted:#b3b0a6;
    --brand-ink:#1d2a33;
  }
  html,body{margin:0;padding:0;width:1200px;height:1047px;overflow:hidden;background:var(--page-bg);}
  .canvas{position:relative;width:1200px;height:1047px;}
  .card{
    position:absolute;left:128px;top:267px;width:944px;height:513px;
    border-radius:22px;overflow:hidden;background:var(--card-bg);
    box-shadow:0 10px 30px rgba(0,0,0,.12);
    font-family:'Lato',sans-serif;
  }
  .card-panel{position:absolute;inset:0;width:944px;height:513px;}
  .identity{position:absolute;left:56px;top:76px;}
  .identity-name{margin:0;font-size:43px;font-weight:700;color:var(--accent-teal);letter-spacing:.5px;line-height:1;}
  .identity-role{margin:12px 0 0;font-size:22px;color:var(--text-muted);}
  .address{position:absolute;left:56px;top:246px;margin:0;font-size:22px;line-height:30px;color:var(--text-muted);font-style:normal;}
  .contacts{position:absolute;left:56px;top:330px;margin:0;padding:0;list-style:none;}
  .contact-item{display:flex;align-items:center;height:35px;font-size:22px;color:var(--text-muted);}
  .contact-icon{width:24px;height:24px;margin-right:21px;flex:none;}
  .brand{position:absolute;left:548px;top:232px;display:flex;align-items:center;}
  .brand-dot{width:44px;height:44px;border-radius:50%;background:var(--accent-teal);margin-right:24px;}
  .brand-name{font-size:34px;font-weight:400;letter-spacing:6px;color:var(--brand-ink);}
</style>
</head>
<body>
<div class="canvas">
  <div class="card">
    <svg class="card-panel" viewBox="0 0 944 513" aria-hidden="true">
      <defs>
        <linearGradient id="panelShade" x1="0" y1="0" x2="1" y2="1">
          <stop offset="0" stop-color="var(--panel-dark)"/>
          <stop offset="0.6" stop-color="var(--panel-mid)"/>
          <stop offset="1" stop-color="var(--panel-dark)"/>
        </linearGradient>
      </defs>
      <path d="M0,0 H536 Q364,256 536,513 H0 Z" fill="var(--accent-teal)"/>
      <path d="M0,0 H520 Q348,256 520,513 H0 Z" fill="url(#panelShade)"/>
    </svg>

    <div class="identity">
      <h1 class="identity-name">JOHN SMITH</h1>
      <p class="identity-role">Founder &amp; CEO</p>
    </div>

    <address class="address">1234 First Line Address<br>5678 Second Line Address</address>

    <ul class="contacts">
      <li class="contact-item">
        <svg class="contact-icon" viewBox="0 0 24 24" fill="none" stroke="var(--accent-teal)" stroke-width="2" stroke-linecap="round"><path d="M5 3h4l2 5-2.5 1.5a11 11 0 0 0 6 6L16 13l5 2v4a2 2 0 0 1-2 2A16 16 0 0 1 3 5a2 2 0 0 1 2-2z"/></svg>
        1234567890
      </li>
      <li class="contact-item">
        <svg class="contact-icon" viewBox="0 0 24 24" fill="var(--accent-teal)"><path d="M2 5h20v14H2z"/><path d="M2 5l10 8 10-8" fill="none" stroke="var(--panel-dark)" stroke-width="1.6"/></svg>
        info@yourmail.com
      </li>
      <li class="contact-item">
        <svg class="contact-icon" viewBox="0 0 24 24" fill="none" stroke="var(--accent-teal)" stroke-width="1.8"><circle cx="12" cy="12" r="9"/><path d="M3 12h18M12 3c3 3 3 15 0 18M12 3c-3 3-3 15 0 18"/></svg>
        www.yourwebsite.com
      </li>
    </ul>

    <div class="brand">
      <span class="brand-dot"></span>
      <span class="brand-name">TIDAL CREST</span>
    </div>
  </div>
</div>
</body>
</html>
```